Financial services referral site needs a redesign

We need a complete re-brand ; new word press design for our existing site. Need a web 2.0 clean crisp look that will convert highly. Consumers with debt come to our site so we can refer them to 3rd party providers of debt solutions ranging from credit counseling, debt consolidation, refinance and student loan consolidation. I would like to see designs that use the color green and final product should communicate safety, trust and privacy. Show case our A+ ZVQ rating etc. See current site at trellisvalleyhelp.com

- I would like to use light blue color scheme to match the logo. The green is making it look off - I definitely need the lead form to be on the top right side of the page

```html
<!DOCTYPE html>
<html lang="en">
<head>
<meta charset="utf-8">
<title>Trellis Valley Help – Debt Consolidation &amp; Credit Counselling</title>
<link rel="stylesheet" href="https://fonts.googleapis.com/css2?family=Arimo:wght@400;700&family=Open+Sans:wght@300;600;700&family=PT+Sans:wght@400;700&family=Tinos&display=swap">
<style>
:root{
  --blue:#0b77d1;
  --blue-dark:#0a5fae;
  --teal:#7fc4cc;
  --teal-deep:#1fb3bf;
  --teal-text:#2a7fb0;
  --hero-dark:#3b3b3e;
  --hero-mid:#525256;
  --band:#e7e7e7;
  --ink:#111;
  --muted:#6d6d6d;
  --tile:#f3f4f5;
  --tile-line:#dcdfe2;
  --footer:#232323;
  --white:#fff;
}
*{box-sizing:border-box;margin:0;padding:0}
html,body{width:895px;height:1200px;overflow:hidden;background:var(--white)}
body{position:relative;font-family:"Arimo",Arial,sans-serif;color:var(--ink)}
.abs{position:absolute}

/* header */
.brand{left:74px;top:20px;display:flex;align-items:center;gap:14px}
.brand-mark{width:68px;height:68px;border-radius:50%;background:var(--teal)}
.brand-name{font-family:"Tinos",serif;font-size:22px;color:var(--teal-text);letter-spacing:-.2px}
.account-tab{left:671px;top:0;width:150px;height:41px;background:var(--teal-deep);border-radius:0 0 6px 6px;text-align:center;color:var(--white)}
.account-tab .links{font-family:"PT Sans",sans-serif;font-weight:700;font-size:10.5px;padding-top:2px}
.account-tab .phone{font-family:"Arimo",sans-serif;font-size:15px;color:#113a4a;margin-top:2px;letter-spacing:.3px}
.search{left:512px;top:60px;width:171px;height:24px;border:1px solid #c9c9c9;border-radius:12px;background:linear-gradient(#fff,#eee)}
.search svg{position:absolute;right:12px;top:4px}
.social{left:703px;top:61px;display:flex;gap:8px}
.social span{width:20px;height:20px;border-radius:50%}

/* nav */
.nav{left:0;top:104px;width:895px;height:36px;background:var(--blue);display:flex;align-items:center;padding-left:75px}
.nav a{font-family:"Open Sans",sans-serif;font-weight:600;font-size:10.4px;color:var(--white);text-decoration:none;padding:0 18px;line-height:26px;border-right:1px solid rgba(255,255,255,.28)}
.nav a:last-child{border-right:0}
.nav a.current{border:1px solid #0c3f73;background:var(--blue-dark);border-radius:4px;box-shadow:inset 0 0 0 1px rgba(255,255,255,.2);margin-right:8px}

/* hero */
.hero{left:0;top:140px;width:895px;height:312px;background:radial-gradient(circle at 30% 40%,var(--hero-mid),var(--hero-dark));overflow:hidden}
.hero svg.photo{position:absolute;left:0;top:0}
.hero-title{left:82px;top:26px;font-family:"PT Sans",sans-serif;font-weight:700;font-size:27px;line-height:29px;color:var(--white)}
.hero-sub{left:82px;top:178px;font-family:"PT Sans",sans-serif;font-weight:700;font-size:17px;line-height:21px;color:var(--white)}
.hero-cta{left:82px;top:236px;width:181px;height:33px;background:var(--blue);color:var(--white);font-family:"PT Sans",sans-serif;font-weight:700;font-size:13.5px;display:flex;align-items:center;justify-content:center;gap:6px;text-decoration:none}
.band{left:0;top:452px;width:895px;height:18px;background:var(--band)}

/* intro */
.intro{left:85px;top:490px;width:415px}
.serif-head{font-family:"Tinos",serif;font-size:22px;line-height:27px;font-weight:400;letter-spacing:.3px}
.intro p{font-size:10.2px;line-height:15px;margin-top:14px}
.intro p + p{margin-top:14px}

/* lead form */
.lead-form{left:542px;top:488px;width:257px;height:268px;background:var(--teal);border-radius:8px;padding:13px 0 0 20px}
.lead-form h2{font-family:"Tinos",serif;font-weight:400;font-size:21px;color:var(--white);margin-bottom:15px}
.field{width:216px;height:24px;background:var(--white);border:1px solid #cfe3e6;font-size:10.3px;color:#a9a9a9;padding:5px 7px;margin-bottom:9px}
.select-row{display:flex;gap:9px}
.select-row .field{width:99px;position:relative}
.select-row .field::after{content:"";position:absolute;right:6px;top:10px;border:4px solid transparent;border-top-color:#666}
.submit{width:213px;height:29px;background:#000;color:var(--white);border-radius:3px;font-family:"PT Sans",sans-serif;font-size:16px;text-align:center;line-height:29px;margin-top:3px}

/* trust line */
.trust{left:542px;top:764px;width:257px;display:flex;align-items:center;justify-content:center;gap:7px;font-family:"PT Sans",sans-serif;font-size:11px;color:var(--muted)}
.trust .seal{width:14px;height:14px;border-radius:50%;background:var(--teal-deep)}
.trust b{color:var(--teal-text);font-weight:700}

.rule{left:87px;top:793px;width:715px;border-top:1px dashed #cfcfcf}

/* benefits */
.benefit{left:77px;width:268px;height:50px}
.benefit .tile{position:absolute;left:26px;top:0;width:242px;height:50px;background:var(--tile);border:1px solid var(--tile-line);border-radius:3px;display:flex;align-items:center;padding-left:40px;font-family:"PT Sans",sans-serif;font-size:15px;color:var(--muted);line-height:17px;letter-spacing:.4px}
.benefit .tile b{font-weight:400;color:#333}
.benefit .badge{position:absolute;left:0;top:0;width:50px;height:50px;border-radius:50%;background:var(--blue);border:2px solid #d8e9f7;display:flex;align-items:center;justify-content:center}

/* news */
.news{left:386px;top:815px;width:432px}
.news-item{position:absolute;left:0;width:432px}
.news-date{position:absolute;left:0;top:0;width:40px;text-align:center;font-family:"Open Sans",sans-serif;color:#555;font-weight:300}
.news-date .day{font-size:29px;line-height:29px}
.news-date .mon{font-size:17px;line-height:17px}
.news-body{position:absolute;left:48px;top:0;width:370px}
.news-body h3{font-size:9.3px;font-weight:700;color:var(--blue);margin-bottom:4px}
.news-body p{font-size:9.3px;line-height:13.4px;color:#222}
.read-more{position:absolute;left:346px;width:56px;height:20px;background:var(--teal);border-radius:2px;color:var(--white);font-size:9px;text-align:center;line-height:20px}
.news-sep{position:absolute;left:46px;width:386px;border-top:1px solid #e3e3e3}

/* footer */
.footer{left:0;top:1133px;width:895px;height:67px;background:var(--footer);color:var(--white)}
.footer .info{position:absolute;left:90px;top:16px;font-size:10px;line-height:17px}
.footer .social-foot{position:absolute;left:692px;top:21px;display:flex;gap:8px}
.footer .social-foot span{width:20px;height:20px;border-radius:50%;background:#7b7b7b}
</style>
</head>
<body>

<header>
  <div class="abs brand">
    <span class="brand-mark"></span>
    <span class="brand-name">Trellis Valley Help</span>
  </div>
  <div class="abs account-tab">
    <div class="links">Sign Up | Member Login</div>
    <div class="phone">03 5550 1828</div>
  </div>
  <div class="abs search">
    <svg width="14" height="14" viewBox="0 0 14 14"><circle cx="5.5" cy="5.5" r="4" fill="none" stroke="#333" stroke-width="1.4"/><line x1="8.5" y1="8.5" x2="13" y2="13" stroke="#333" stroke-width="2"/></svg>
  </div>
  <div class="abs social">
    <span style="background:#3b5a98"></span>
    <span style="background:#29a9e1"></span>
    <span style="background:#dd4b39"></span>
    <span style="background:#f57d00"></span>
  </div>
</header>

<nav class="abs nav">
  <a class="current">HOME</a>
  <a>ABOUT US</a>
  <a>SERVICES</a>
  <a>HOURS &amp; LOCATION</a>
  <a>HOME DEBT LOANS</a>
  <a>SERVICES</a>
  <a>CONTACT US</a>
</nav>

<section class="abs hero">
  <svg class="photo" width="895" height="312" viewBox="0 0 895 312">
    <defs>
      <linearGradient id="photoTone" x1="0" y1="0" x2="1" y2="1">
        <stop offset="0" stop-color="#b7b0a4"/>
        <stop offset=".5" stop-color="#7d7a78"/>
        <stop offset="1" stop-color="#2d3a55"/>
      </linearGradient>
    </defs>
    <path d="M302,0 Q296,205 418,312 L895,312 L895,0 Z" fill="#8fc7cd"/>
    <path role="img" aria-label="Photo: business team at a desk reviewing papers and working on a laptop" d="M318,0 Q314,198 436,312 L895,312 L895,0 Z" fill="url(#photoTone)"/>
  </svg>
  <h1 class="abs hero-title">DEBT<br>CONSOLIDATION<br>&amp; CREDIT<br>COUNSELLING<br>INFORMATION</h1>
  <p class="abs hero-sub">Debt problems?<br>Let us help you find a solution.</p>
  <a class="abs hero-cta">CONTACT AN ADVISOR
    <svg width="14" height="14" viewBox="0 0 14 14"><circle cx="7" cy="7" r="7" fill="#fff"/><path d="M5.5,3.8 L8.8,7 L5.5,10.2" fill="none" stroke="#0b77d1" stroke-width="2"/></svg>
  </a>
</section>
<div class="abs band"></div>

<section class="abs intro">
  <h2 class="serif-head">When To Consider A Debt Consolidation Program</h2>
  <p>If you're struggling to keep up with several credit card bills, personal loans or collection accounts, you've come to the right place. Trellis Valley Help connects you with trusted providers of credit counselling, debt consolidation, refinancing and student loan consolidation, so you can find a plan that fits your budget.</p>
  <p>At Trellis Valley Help, we believe that getting help with debt should be as simple and stress-free as possible. That's why our free service was designed to keep your privacy and security in mind. Whether you want one lower monthly payment or a full review of your options, a qualified advisor will look at your situation and answer all of your questions in a relaxed, pressure-free setting. Through our partner network, we offer:</p>
</section>

<form class="abs lead-form">
  <h2>Our Debt Solution</h2>
  <div class="field">First Name</div>
  <div class="field">First Name</div>
  <div class="field">Address</div>
  <div class="field">Address</div>
  <div class="select-row">
    <div class="field">State</div>
    <div class="field">Debt&nbsp; Amount</div>
  </div>
  <div class="submit">Get Assistance Now !</div>
</form>

<div class="abs trust"><span class="seal"></span><span><b>A+ ZVQ Rating</b> &middot; Secure &amp; Private</span></div>

<div class="abs rule"></div>

<div class="abs benefit" style="top:818px">
  <div class="tile"><span>Reduce high interest<br><b>credit rates</b></span></div>
  <div class="badge"><svg width="24" height="26" viewBox="0 0 24 26"><rect x="3" y="3" width="15" height="20" rx="2" fill="none" stroke="#fff" stroke-width="2"/><line x1="6" y1="9" x2="15" y2="9" stroke="#fff" stroke-width="1.6"/><line x1="6" y1="13" x2="12" y2="13" stroke="#fff" stroke-width="1.6"/><circle cx="17" cy="19" r="6" fill="#fff"/><path d="M14,19 L16.3,21.3 L20,17" fill="none" stroke="#0b77d1" stroke-width="1.8"/></svg></div>
</div>
<div class="abs benefit" style="top:890px">
  <div class="tile">Stop harassing credit calls</div>
  <div class="badge"><svg width="24" height="24" viewBox="0 0 24 24"><rect x="1" y="1" width="10" height="10" rx="1.5" fill="#fff"/><rect x="13" y="1" width="10" height="10" rx="1.5" fill="#fff"/><rect x="1" y="13" width="10" height="10" rx="1.5" fill="#fff"/><rect x="13" y="13" width="10" height="10" rx="1.5" fill="#fff"/><path d="M6,3.5v5M3.5,6h5M15.5,6h5M3.5,18h5M15.5,16.5h5M15.5,19.5h5" stroke="#0b77d1" stroke-width="1.5"/></svg></div>
</div>
<div class="abs benefit" style="top:961px">
  <div class="tile">One low monthly payment</div>
  <div class="badge"><svg width="26" height="24" viewBox="0 0 26 24"><path d="M13,1 L25,7 H1 Z" fill="#fff"/><rect x="4" y="9" width="3" height="10" fill="#fff"/><rect x="9.5" y="9" width="3" height="10" fill="#fff"/><rect x="15" y="9" width="3" height="10" fill="#fff"/><rect x="20" y="9" width="3" height="10" fill="#fff"/><rect x="1" y="20" width="24" height="3" fill="#fff"/></svg></div>
</div>
<div class="abs benefit" style="top:1032px">
  <div class="tile">No costs unless you save</div>
  <div class="badge"><svg width="22" height="26" viewBox="0 0 22 26"><path d="M6,14 L2,23 L6,22 L8,25 L11,17 L14,25 L16,22 L20,23 L16,14" fill="#fff"/><circle cx="11" cy="9" r="8" fill="#fff"/><circle cx="11" cy="9" r="4.5" fill="none" stroke="#0b77d1" stroke-width="1.5"/></svg></div>
</div>

<section class="abs news">
  <h2 class="serif-head">Current Debt Relief News</h2>
  <article class="news-item" style="top:37px">
    <div class="news-date"><div class="day">20</div><div class="mon">JAN</div></div>
    <div class="news-body">
      <h3>Lorem ipsum dolor sit amet</h3>
      <p>consectetur adipisicing elit, sed do eiusmod tempor incididunt ut labore et dolore magna aliqua. Ut enim ad minim veniam, quis nostrud exercitation ullamco laboris nisi ut aliquip ex ea commodo consequat. Duis aute irure dolor in reprehenderit in voluptate velit esse cillum dolore eu fugiat nulla pariatur. Excepteur sint occaecat cupidatat non proident, sunt in culpa qui officia deserunt mollit anim id est laborum Duis aute irure dolor in reprehenderit in voluptate.</p>
    </div>
    <div class="read-more" style="top:88px">Read More</div>
    <div class="news-sep" style="top:118px"></div>
  </article>
  <article class="news-item" style="top:178px">
    <div class="news-date"><div class="day">20</div><div class="mon">JAN</div></div>
    <div class="news-body">
      <h3>Lorem ipsum dolor sit amet</h3>
      <p>consectetur adipisicing elit, sed do eiusmod tempor incididunt ut labore et dolore magna aliqua. Ut enim ad minim veniam, quis nostrud exercitation ullamco laboris nisi ut aliquip ex ea commodo consequat. Duis aute irure dolor in reprehenderit in voluptate velit esse cillum dolore eu fugiat nulla pariatur. Excepteur sint occaecat cupidatat non proident, sunt in culpa qui officia deserunt mollit anim id est laborum Duis aute irure dolor in reprehenderit in voluptate.</p>
    </div>
    <div class="read-more" style="top:91px">Read More</div>
  </article>
</section>

<footer class="abs footer">
  <div class="info">Trellis Valley Help - Tel: (305) 555-0142 - 210 Harbor Lane #12, Bayview, FL 33000<br>Privacy Policy | Sitemap | Terms of Use</div>
  <div class="social-foot"><span></span><span></span><span></span><span></span></div>
</footer>

</body>
</html>
```